White Paper and One-Page Advertisement for TELVARIS-QP

I need both documents to be better formatted and designed so they look professional, not something someone with mediocre word skills put together. They will go out to 1000s of industry professionals, and they need to look sharp. I need them to have my company's color palate logo, and branding on it similar to how it is now, but better. Please do not change any of the written content, but it can be arranged in any other format you think is better. Smart art and things i've already used can be omitted in favor of better designs. The developer is free to use their creativity. White paper should not be longer than the three pages unless necessary.

Target Market(s)

Life Sciences supply chain professionals

Colors
33b8a4
0592cd
9bcb3c
fbee3e
3277b5

Requirements
Must have
• Must be professional looking and not look like something done in word. Please use the color palate as seen on the documents.
Should not have
• Any changes to the written content.

```html
<!DOCTYPE html>
<html lang="en">
<head>
<meta charset="utf-8">
<title>Changing Pharma's Paradigm of Waste — TELVARIS-QP</title>
<link rel="stylesheet" href="https://fonts.googleapis.com/css2?family=Saira:wght@300;400;700;800&display=swap">
<style>
  :root {
    --stage: #2b2b2b;
    --paper: #ffffff;
    --brand-teal: #0f7a68;
    --band-teal: #0b7a6b;
    --green-light: #7dbb4a;
    --green-deep: #2f9670;
    --ring-green: #5fae3e;
    --ring-dark: #1c7a62;
    --photo-warm: #8a6a52;
    --photo-cool: #b9c2c4;
    --text-light: #ffffff;
  }
  html, body {
    margin: 0;
    width: 1200px;
    height: 1200px;
    overflow: hidden;
    background: var(--stage);
  }
  .cover {
    position: absolute;
    left: 195px;
    top: 28px;
    width: 810px;
    height: 1144px;
    background: var(--paper);
    overflow: hidden;
    font-family: "Saira", sans-serif;
  }
  .cover-art {
    position: absolute;
    inset: 0;
  }
  .brand {
    position: absolute;
    top: 112px;
    right: 30px;
    display: flex;
    align-items: center;
    gap: 10px;
  }
  .brand-dot {
    width: 22px;
    height: 22px;
    border-radius: 50%;
    background: var(--brand-teal);
  }
  .brand-name {
    font-size: 34px;
    font-weight: 700;
    letter-spacing: 1px;
    color: var(--brand-teal);
    line-height: 1;
  }
  .title {
    position: absolute;
    left: 0;
    right: 0;
    top: 858px;
    margin: 0;
    text-align: center;
    color: var(--text-light);
    line-height: 1;
  }
  .title-lead {
    display: block;
    font-size: 46px;
    font-weight: 300;
    letter-spacing: 1px;
  }
  .title-main {
    display: block;
    margin-top: 4px;
    font-size: 52px;
    font-weight: 800;
    letter-spacing: 1.5px;
  }
  .subtitle-band {
    position: absolute;
    left: 0;
    right: 0;
    top: 968px;
    height: 62px;
    background: var(--band-teal);
    display: flex;
    align-items: center;
    justify-content: center;
  }
  .subtitle {
    margin: 0;
    text-align: center;
    color: var(--text-light);
    font-size: 19.5px;
    font-weight: 400;
    line-height: 1.15;
    letter-spacing: 0.6px;
  }
  .byline {
    position: absolute;
    left: 0;
    right: 0;
    top: 1042px;
    text-align: center;
    color: var(--text-light);
    line-height: 1;
  }
  .author {
    display: block;
    font-size: 28px;
    font-weight: 800;
    letter-spacing: 0.5px;
  }
  .date {
    display: block;
    margin-top: 12px;
    font-size: 38px;
    font-weight: 800;
    letter-spacing: 1px;
  }
</style>
</head>
<body>
  <article class="cover">
    <svg class="cover-art" width="810" height="1144" viewBox="0 0 810 1144">
      <defs>
        <linearGradient id="greenField" x1="0" y1="0" x2="0" y2="1">
          <stop offset="0" stop-color="var(--green-light)"/>
          <stop offset="1" stop-color="var(--green-deep)"/>
        </linearGradient>
        <radialGradient id="ceremonyTones" cx="0.45" cy="0.55" r="0.6">
          <stop offset="0" stop-color="#b7957a"/>
          <stop offset="0.6" stop-color="var(--photo-warm)"/>
          <stop offset="1" stop-color="#3e2a2a"/>
        </radialGradient>
        <radialGradient id="wardTones" cx="0.45" cy="0.5" r="0.6">
          <stop offset="0" stop-color="#e3d6c8"/>
          <stop offset="1" stop-color="var(--photo-cool)"/>
        </radialGradient>
      </defs>

      <path class="green-field" d="M0,495 C160,860 560,900 810,640 L810,1144 L0,1144 Z" fill="url(#greenField)"/>

      <circle class="main-photo-mat" cx="351" cy="447" r="336" fill="var(--paper)"/>
      <circle class="main-photo-ring" cx="351" cy="447" r="319" fill="none" stroke="var(--ring-dark)" stroke-width="2.5"/>
      <circle class="main-photo" cx="351" cy="447" r="302" fill="url(#ceremonyTones)"
              role="img" aria-label="Photo: smiling bride in a gold headdress with two women at a family ceremony"/>

      <circle class="inset-photo-mat" cx="608" cy="653" r="186" fill="var(--paper)"/>
      <circle class="inset-photo-ring" cx="608" cy="653" r="176" fill="none" stroke="var(--ring-green)" stroke-width="2.5"/>
      <circle class="inset-photo" cx="608" cy="653" r="163" fill="url(#wardTones)"
              role="img" aria-label="Photo: smiling young patient sitting up in a hospital bed"/>
    </svg>

    <div class="brand">
      <span class="brand-dot"></span>
      <span class="brand-name">TELVARIS-QP</span>
    </div>

    <h1 class="title">
      <span class="title-lead">CHANGING PHARMA’S</span>
      <span class="title-main">PARADIGM OF WASTE</span>
    </h1>

    <div class="subtitle-band">
      <p class="subtitle">How Pharma’s Demand Volatility Could Be Costing<br>You Millions in Material Write-downs &amp; Procurement</p>
    </div>

    <div class="byline">
      <span class="author">Dana Whitfield</span>
      <span class="date">AUGUST 2018</span>
    </div>
  </article>
</body>
</html>
```